Law Firm Stationery Design Project

This is the final part of a law firm rebrand project. The logo design is near completion, and I am also asking for business card designs in a separate contest. I will post the winning logo design to this project sometime tomorrow.

The job here is to design letterhead, business envelopes, shipping labels, memorandum, report, and the like, based on the following criteria (mainly quoted from the business card project):

My firm specializes in representing startup companies. This means I routinely interact with young entrepreneurs and the (typically) older, more experienced investors who fund them. I need to appeal to the former without offending the latter. I'm interesting in conveying the idea that my firm is a credible alternative to larger, brand-name firms. I use these words in positioning my firm in this market: creative; flexible; fair; practical; experienced. The winning design needs to convey this idea.

I'm will also be re-working my website soon and will likely use noto sans and noto serif as my primary website fonts. I'd like the stationary (just as I have asked the same of the business card) to use a font that is similar, but also compatible with the font used in the firm's logo.

Target Market(s)

Young entrepreneurs and older investors who collaborate in the formation and funding of high-tech startup companies located in the Pacific Northwest.

Industry/Entity Type

Law Firm

Font styles to use
Serif
Sans Serif

Requirements
Must have
• - Firm logo, firm tag line, return mailing address, firm website url, firm phone number, attorney name, attorney title, attorney email address, and attorney twitter account. I will provide the specific contact information to the winning designer; you may use fictional data in preparing your design.

The attached pdf for a proposed business card indicates the kind of tone that I have in mind, recognizing that it is my amateur attempt at doing what I'm hoping the winning designer is able to do so much better.

```html
<!DOCTYPE html>
<html lang="en">
<head>
<meta charset="utf-8">
<title>Halvorsen Law PLLC — Letterhead</title>
<link rel="stylesheet" href="https://fonts.googleapis.com/css2?family=Montserrat:wght@300;400;500;600;700&display=swap">
<style>
  :root {
    --backdrop: #e9eaec;
    --paper: #ffffff;
    --ink: #3b4a5f;
    --ink-soft: #6d7888;
    --mark-line: #8a94a3;
    --deco: #e3e6ea;
  }
  * { box-sizing: border-box; margin: 0; padding: 0; }
  html, body {
    width: 1200px;
    height: 849px;
    overflow: hidden;
    background: var(--backdrop);
    font-family: "Montserrat", "Helvetica Neue", Arial, sans-serif;
    color: var(--ink);
  }
  .letterhead {
    position: absolute;
    left: 300px;
    top: 37px;
    width: 600px;
    height: 775px;
    background: var(--paper);
    box-shadow: 0 2px 10px rgba(40, 50, 70, 0.08);
    overflow: hidden;
    padding: 46px 56px 0 56px;
  }
  .masthead {
    position: relative;
    height: 140px;
  }
  .brand {
    position: absolute;
    left: 0;
    top: 0;
  }
  .firm-mark {
    display: flex;
    align-items: center;
    gap: 8px;
    white-space: nowrap;
  }
  .firm-mark__square {
    width: 13px;
    height: 13px;
    border: 1.5px solid var(--mark-line);
    flex: none;
  }
  .firm-mark__name {
    font-size: 17px;
    font-weight: 400;
    letter-spacing: 0.1em;
    text-transform: uppercase;
    color: var(--ink-soft);
  }
  .firm-tagline {
    margin-top: 4px;
    padding-left: 21px;
    font-size: 5.5px;
    font-weight: 600;
    letter-spacing: 0.14em;
    text-transform: uppercase;
    color: var(--ink-soft);
    white-space: nowrap;
  }
  .contact {
    position: absolute;
    right: 0;
    top: 96px;
    display: grid;
    grid-template-columns: auto auto;
    column-gap: 26px;
    row-gap: 4px;
    font-size: 7px;
    font-style: normal;
    color: var(--ink-soft);
  }
  .contact__item {
    display: flex;
    align-items: center;
    gap: 5px;
    white-space: nowrap;
  }
  .contact__item svg {
    width: 8px;
    height: 8px;
    flex: none;
    stroke: var(--mark-line);
    fill: none;
    stroke-width: 1.2;
  }
  .letter {
    margin-top: 8px;
    font-size: 11px;
    line-height: 1.55;
  }
  .letter__salutation {
    font-weight: 700;
    font-size: 12px;
    margin-bottom: 12px;
  }
  .letter p { margin-bottom: 12px; }
  .deco-square {
    position: absolute;
    left: 40px;
    bottom: -70px;
    width: 190px;
    height: 190px;
    border: 6px solid var(--deco);
    transform: rotate(45deg);
  }
</style>
</head>
<body>
  <main class="letterhead">
    <header class="masthead">
      <div class="brand">
        <div class="firm-mark">
          <span class="firm-mark__square"></span>
          <span class="firm-mark__name">Halvorsen Law PLLC</span>
        </div>
        <div class="firm-tagline">Practical counsel for new ventures</div>
      </div>
      <address class="contact">
        <span class="contact__item">
          <svg viewBox="0 0 10 10"><path d="M5 9.5 C2 6 1.5 4.8 1.5 3.8 A3.5 3.5 0 0 1 8.5 3.8 C8.5 4.8 8 6 5 9.5Z"/><circle cx="5" cy="3.8" r="1.2"/></svg>
          412 Harbor Ave., STE 900 Portland, Oregon 97204
        </span>
        <span></span>
        <span class="contact__item">
          <svg viewBox="0 0 10 10"><path d="M2 1 L4 1 L4.8 3.2 L3.6 4.2 C4.2 5.5 4.8 6.1 6 6.6 L7 5.4 L9 6.2 L9 8.2 C5 8.6 1.4 5 1.8 1Z"/></svg>
          503.555.0147
        </span>
        <span class="contact__item">
          <svg viewBox="0 0 10 10"><circle cx="5" cy="5" r="4"/><path d="M1 5 H9 M5 1 C3 3.5 3 6.5 5 9 M5 1 C7 3.5 7 6.5 5 9"/></svg>
          www.halvorsenlawpllc.com
        </span>
        <span class="contact__item">
          <svg viewBox="0 0 10 10"><rect x="1" y="2" width="8" height="6"/><path d="M1 2 L5 5.5 L9 2"/></svg>
          mara@halvorsenlawpllc.com
        </span>
        <span class="contact__item">
          <svg viewBox="0 0 10 10"><path d="M1.5 7.5 C4 8 7.5 6.5 7.5 3 L8.8 2 L7.3 2.2 C6.5 1.2 4.6 1.6 4.8 3.4 C3.4 3.3 2.4 2.7 1.6 1.8 C1.1 3 1.8 4.4 2.6 4.6 C3 6 2.6 6.8 1.5 7.5Z"/></svg>
          @marahalvorsen
        </span>
      </address>
    </header>

    <section class="letter">
      <p class="letter__salutation">Dear Sir/Madam,</p>
      <p>Vivamus sagittis lacus vel augue laoreet rutrum faucibus dolor auctor</p>
      <p>Lorem ipsum dolor sit amet, consectetuer adipiscing elit, sed diam nonummy nibh euismod tincidunt ut laoreet dolore magna aliquam erat volutpat. Ut wisi enim ad minim veniam, quis nostrud exerci tation ullam corper suscipit lobortis nisl ut aliquip ex ea commodo consequat.</p>
      <p>Integer posuere erat a ante venenatis dapibus posuere velit aliquet. Lorem ipsum dolor sit amet, consectetur adipiscing elit.</p>
      <p>Vivamus sagittis lacus vel augue laoreet rutrum faucibus dolor auctor. Donec id elit non mi porta gravida at eget metus. Donec ullamcorper nulla non metus auctor fringilla. Morbi leo risus, porta ac consectetur ac, vestibulum at eros. Nullam id dolor id nibh ultricies vehicula ut id elit. Nullam quis risus eget urna mollis ornare vel eu leo. Vivamus sagittis lacus vel augue laoreet rutrum faucibus dolor auctor.</p>
      <p>Donec id elit non mi porta gravida at eget metus. Vivamus sagittis lacus vel augue laoreet rutrum faucibus dolor auctor. Integer posuere erat a ante venenatis dapibus posuere velit aliquet. Donec id elit non mi porta gravida at eget metus. Aenean lacinia bibendum nulla sed consectetur.</p>
      <p>Lorem ipsum dolor sit amet, consectetuer adipiscing elit, sed diam nonummy nibh euismod tincidunt ut laoreet dolore magna aliquam erat volutpat. Ut wisi enim ad minim veniam, quis nostrud exerci tation ullam corper suscipit lobortis nisl ut aliquip ex ea commodo consequat.</p>
    </section>

    <div class="deco-square" aria-hidden="true"></div>
  </main>
</body>
</html>
```